December online webinar for our coaching and mentoring business.

needing an email flyer and something to use on appropriate social media e.g. Instagram to promote our December half day webinar focusing on positive mindset, relationships and 2021 being a new year with new opportunities. For the feel of what we have done previously:
www.qlvgetaways.com.au
We will be using 2 guest speakers:
Marcus Elwood of BucketGoals.com and
Lorena Voss, psychologist and both will need to be prominent on the marketing material we send out on email and use on social media.
The webinar will likely run Thursday December 10th from 12.30pm to 4.30pm AEST and will be hosted and facilitated by me and on behalf of Tarrow Business Coaching.
I am thinking colour schemes and branding similar to what you see on the website above.
Pricing needs to be on the flyer - $750 + GST per person*
*enquire for multi booking discounts for 2 people or more

Target Market(s)

people looking for a boost before the year end and a fast start to 2021

Font styles to use
Sans Serif

Requirements
Must have
• see brief above
Nice to have
• see brief above
Should not have
• see brief above

```html
<!DOCTYPE html>
<html lang="en">
<head>
<meta charset="utf-8">
<title>Tarrow Business Coaching – December Webinar</title>
<link rel="stylesheet" href="https://fonts.googleapis.com/css2?family=Poppins:wght@300;400;600;700&display=swap">
<style>
  :root {
    --brand-red: #e8403a;
    --accent-red: #d93333;
    --ink: #0d0d0d;
    --muted: #8f8f8f;
    --paper: #ffffff;
    --photo-grey: #d9d6d0;
    --photo-yellow: #f2e93a;
    --photo-blue: #1e6f93;
    --photo-charcoal: #4a4c55;
  }
  * { margin: 0; padding: 0; box-sizing: border-box; }
  html, body { width: 686px; height: 1200px; overflow: hidden; background: var(--paper); }
  body { font-family: "Poppins", sans-serif; color: var(--ink); }
  .flyer { position: relative; width: 686px; height: 1200px; overflow: hidden; background: var(--paper); }
  .shapes { position: absolute; inset: 0; }
  .brand-name {
    position: absolute; left: 28px; top: 96px; width: 200px;
    color: var(--paper); font-weight: 600; font-size: 26px; line-height: 1.15;
  }
  .intro {
    position: absolute; right: 78px; top: 82px; text-align: right;
    color: var(--muted); font-weight: 300; font-size: 21px; line-height: 31px;
  }
  .headline {
    position: absolute; right: 78px; top: 146px; text-align: right;
    font-weight: 700; font-size: 54px; line-height: 67px; letter-spacing: -0.5px;
  }
  .subhead {
    position: absolute; right: 78px; top: 350px; text-align: right;
    font-weight: 400; font-size: 31px; line-height: 47px;
  }
  .speaker { position: absolute; }
  .speaker-name { color: var(--brand-red); font-size: 29px; line-height: 1.1; white-space: nowrap; }
  .speaker-name strong { font-weight: 700; }
  .speaker-name span { font-weight: 300; }
  .speaker-role { font-size: 18px; font-weight: 300; line-height: 1.4; }
  .speaker--psych { right: 398px; top: 530px; text-align: right; }
  .speaker--goals { left: 388px; top: 855px; }
  .event-details {
    position: absolute; left: 64px; top: 985px; color: var(--brand-red);
    font-size: 32px; line-height: 36px; letter-spacing: -0.5px;
  }
  .event-details strong { font-weight: 700; }
  .event-details .light { font-weight: 300; }
  .pricing {
    position: absolute; left: 64px; top: 1095px;
    font-size: 15.5px; font-weight: 300; line-height: 22px; color: #333;
  }
</style>
</head>
<body>
<main class="flyer">
  <svg class="shapes" width="686" height="1200" viewBox="0 0 686 1200" aria-hidden="false">
    <defs>
      <linearGradient id="psych-photo" x1="0" y1="0" x2="0" y2="1">
        <stop offset="0" stop-color="var(--photo-grey)"/>
        <stop offset="0.45" stop-color="#d8b88a"/>
        <stop offset="0.6" stop-color="var(--photo-blue)"/>
        <stop offset="1" stop-color="#16506b"/>
      </linearGradient>
      <linearGradient id="goals-photo" x1="0" y1="0" x2="0" y2="1">
        <stop offset="0" stop-color="var(--photo-yellow)"/>
        <stop offset="0.35" stop-color="#c9a58c"/>
        <stop offset="0.55" stop-color="var(--photo-charcoal)"/>
        <stop offset="1" stop-color="#3b3d45"/>
      </linearGradient>
    </defs>
    <polygon class="brand-corner" points="0,0 391,0 0,358" fill="var(--brand-red)"/>
    <polygon class="photo-psych" role="img" aria-label="Portrait photo of psychologist Lorena Voss" points="306,532 610,587 414,827" fill="url(#psych-photo)"/>
    <polygon class="photo-goals" role="img" aria-label="Photo of Marcus Elwood speaking on stage" points="115,732 398,662 346,968" fill="url(#goals-photo)"/>
    <g class="accent-triangles" fill="var(--accent-red)">
      <polygon points="553,520 613,495 606,558"/>
      <polygon points="175,633 212,615 209,654"/>
      <polygon points="503,749 542,747 525,782"/>
      <polygon points="82,791 164,820 99,876"/>
    </g>
  </svg>

  <div class="brand-name">Tarrow Business Coaching</div>

  <p class="intro">December half day<br>Webinar focusing on</p>
  <h1 class="headline">Positive<br>Mindset,<br>Relationships</h1>
  <p class="subhead">and 2021 being a new year<br>with new opportunities</p>

  <div class="speaker speaker--psych">
    <p class="speaker-name"><strong>LORENA</strong> <span>Voss</span></p>
    <p class="speaker-role">Psychologist</p>
  </div>
  <div class="speaker speaker--goals">
    <p class="speaker-name"><strong>MARCUS</strong> <span>Elwood</span></p>
    <p class="speaker-role">BucketGoals.com</p>
  </div>

  <div class="event-details">
    <p><strong>December 10th</strong></p>
    <p class="light">Thursday from</p>
    <p><strong>12.30pm to 4.30pm</strong> <span class="light">AEST</span></p>
  </div>

  <p class="pricing">Pricing needs to be on the flyer - $750 + GST per person*<br>*enquire for multi booking discounts for 2 people or more</p>
</main>
</body>
</html>
```